Beer Can Label named: ZAP Ginger Beer

We need a funky design for a Ginger Beer that is made from all natural ingredients. The label needs to be full of Colour, emphasis on the Ginger Root. ZAP (Zested And Poured)

Target Market(s)

None beer drinkers'

Requirements
Must have
• Name on the label must beer easy to read. Needs to be very colourful, playful & even a bit cheaky.
Nice to have
• A label that looks at the benefits of Ginger for the body in a fun artistic design.
Should not have
• Should NOT be a simple, basic, minimalistic design

```html
<!DOCTYPE html>
<html lang="en">
<head>
<meta charset="utf-8">
<title>ZAP Ginger Beer – Can Label</title>
<link rel="stylesheet" href="https://fonts.googleapis.com/css2?family=Roboto:wght@700&display=swap">
<style>
  :root {
    --backdrop: #f3f3f3;
    --label-top: #fffaf0;
    --label-mid: #fff1d9;
    --label-bottom: #ffe2b8;
    --label-edge: #e6d6bd;
    --ginger-orange: #e8891c;
    --ginger-deep: #c9650d;
    --zest-yellow: #f6c12a;
    --leaf-green: #5fae3a;
    --fizz-pink: #e9477a;
    --chevron-black: #161616;
    --root-light: #e9cd9c;
    --root-dark: #a47a48;
  }
  * { box-sizing: border-box; margin: 0; padding: 0; }
  html, body {
    width: 1200px;
    height: 1200px;
    overflow: hidden;
    background: var(--backdrop);
  }
  .canvas {
    position: relative;
    width: 1200px;
    height: 1200px;
  }
  .label {
    position: absolute;
    left: 220px;
    top: 80px;
    width: 760px;
    height: 1040px;
    background: linear-gradient(180deg, var(--label-top) 0%, var(--label-mid) 55%, var(--label-bottom) 100%);
    border: 1px solid var(--label-edge);
    overflow: hidden;
    font-family: "Roboto", Arial, sans-serif;
    font-weight: 700;
    color: var(--ginger-orange);
  }
  .label__bands {
    position: absolute;
    inset: 0;
    width: 760px;
    height: 1040px;
  }
  .brand-title {
    position: absolute;
    left: 0;
    top: 215px;
    width: 100%;
    text-align: center;
    line-height: 1;
  }
  .brand-title__name {
    display: block;
    font-size: 100px;
    padding-left: 70px;
    white-space: nowrap;
  }
  .brand-title__product {
    display: block;
    font-size: 172px;
    margin-top: -4px;
    padding-left: 20px;
    color: var(--ginger-deep);
  }
  .ginger-root {
    position: absolute;
    left: 520px;
    top: 680px;
    width: 220px;
    height: 170px;
    border-radius: 40% 60% 45% 55% / 55% 45% 55% 45%;
    background: radial-gradient(ellipse at 45% 45%, var(--root-light), var(--root-dark) 80%, transparent 100%);
  }
  .volume {
    position: absolute;
    left: 110px;
    top: 935px;
    font-size: 44px;
  }
</style>
</head>
<body>
  <main class="canvas">
    <section class="label" aria-label="ZAP Ginger Beer can label">
      <svg class="label__bands" viewBox="0 0 760 1040" aria-hidden="true">
        <!-- small left chevron with colour trims -->
        <polyline points="-20,232 78,355 -20,478" fill="none" stroke="var(--zest-yellow)" stroke-width="16"/>
        <polyline points="-20,250 60,355 -20,460" fill="none" stroke="var(--chevron-black)" stroke-width="70"/>
        <polyline points="-20,300 22,355 -20,410" fill="none" stroke="var(--fizz-pink)" stroke-width="14"/>
        <!-- large right chevron with colour trims -->
        <polyline points="790,330 236,770 690,1120" fill="none" stroke="var(--leaf-green)" stroke-width="20"/>
        <polyline points="790,352 268,770 690,1094" fill="none" stroke="var(--zest-yellow)" stroke-width="16"/>
        <polyline points="790,380 300,770 690,1070" fill="none" stroke="var(--chevron-black)" stroke-width="72"/>
        <polyline points="790,432 366,770 690,1018" fill="none" stroke="var(--ginger-orange)" stroke-width="16"/>
        <!-- zesty dots -->
        <circle cx="640" cy="130" r="26" fill="var(--zest-yellow)"/>
        <circle cx="700" cy="190" r="14" fill="var(--leaf-green)"/>
        <circle cx="110" cy="130" r="18" fill="var(--fizz-pink)"/>
        <circle cx="160" cy="620" r="22" fill="var(--leaf-green)"/>
        <circle cx="90" cy="760" r="12" fill="var(--zest-yellow)"/>
        <circle cx="230" cy="860" r="16" fill="var(--fizz-pink)"/>
      </svg>

      <h1 class="brand-title">
        <span class="brand-title__name">ZAP Ginger</span>
        <span class="brand-title__product">Beer</span>
      </h1>

      <div class="ginger-root" role="img" aria-label="Photograph of fresh ginger root"></div>

      <p class="volume">500ml</p>
    </section>
  </main>
</body>
</html>
```